LANTERN: Handwashing Poster (11x17)

- The poster will be 11x17.
- Attached is the general layout and language to be used. (attachment). Please feel to change the layout if there is a better use of space.
- It will use the same color theme as before - see example attachment one. (Less busy background).
- For final products, one poster will be branded 3 different ways (COVID-19, Flu, COVID-19&Flu). See branding logos attachments
- Attached is copy logo - attachment
- Poster must contain the language, "This project is supported by the Marlowe Bureau for Wellness Monitoring and Outreach of the Kestrel Office of Community Vitality and Care (KOV) as part of a financial assistance award totaling $18,420,150 with 100 percent funded by MBW/KOV. The contents are those of the author(s) and do not necessarily represent the official views of, nor an endorsement, by MBW/KOV, or the Kestrel Commonwealth Government."

```html
<!DOCTYPE html>
<html lang="en">
<head>
<meta charset="utf-8">
<title>LANTERN Handwashing Poster</title>
<link href="https://fonts.googleapis.com/css2?family=Archivo:wght@400;600;800;900&family=Libre+Baskerville&family=Poppins:wght@400;500;600&display=swap" rel="stylesheet">
<style>
:root{
  --stage:#8e8e8e;
  --paper:#ffffff;
  --beige:#ece7df;
  --maroon:#8b2a2e;
  --maroon-deep:#3d1216;
  --cyan:#3ec6d3;
  --teal:#5eb2b6;
  --teal-deep:#1d4a4f;
  --ink:#2a1a1b;
  --muted:#444;
}
*{box-sizing:border-box;margin:0;padding:0}
html,body{width:1200px;height:4000px;overflow:hidden}
body{background:var(--stage);font-family:"Poppins",sans-serif;color:var(--ink);position:relative}
.poster{position:absolute;left:208px;width:784px;height:1211px;background:var(--paper);box-shadow:0 6px 18px rgba(0,0,0,.35);overflow:hidden}
.poster--covid{top:109px}
.poster--combo{top:1385px}
.poster--covid-b{top:2664px}

.masthead{display:flex;height:188px}
.masthead__brand{width:515px;background:var(--beige);display:flex;flex-direction:column;align-items:center;padding-top:30px}
.campaign-frame{border:5px solid var(--maroon);border-top:none;padding:4px 22px 10px;text-align:center;position:relative}
.campaign-frame::before{content:"";position:absolute;top:0;left:-5px;width:30px;border-top:5px solid var(--maroon)}
.campaign-frame::after{content:"";position:absolute;top:0;right:-5px;width:30px;border-top:5px solid var(--maroon)}
.campaign-frame__name{font-family:"Archivo",sans-serif;font-weight:900;font-size:62px;line-height:1;color:var(--maroon);letter-spacing:1px}
.campaign-frame__sub{font-family:"Libre Baskerville",serif;font-size:15px;color:var(--maroon);letter-spacing:1px;margin-top:6px}
.poster--combo .campaign-frame__name{color:var(--teal)}
.masthead__tagline{margin-top:auto;margin-bottom:10px;font-family:"Archivo",sans-serif;font-weight:600;font-size:11px;color:var(--maroon);letter-spacing:.3px}
.masthead__partner{flex:1;display:flex;flex-direction:column;align-items:center;justify-content:center;gap:12px}
.partner-mark{width:44px;height:44px;background:var(--teal)}
.partner-name{font-family:"Archivo",sans-serif;font-weight:800;font-size:16px;color:var(--maroon);text-align:center;line-height:1.15}

.band{height:22px;background:linear-gradient(var(--teal) 0 33%,var(--paper) 33% 66%,var(--maroon) 66%)}
.band--foot{position:absolute;bottom:0;left:0;right:0;height:20px}

.content{padding:0 50px}
.headline{margin-top:6px;background:var(--maroon-deep);text-align:center;padding:10px 0 8px;font-family:"Archivo",sans-serif;font-weight:900;font-size:47px;line-height:1}
.headline__top{color:var(--cyan);display:block}
.headline__bottom{color:#fff;display:block}
.intro{font-family:"Archivo",sans-serif;font-weight:800;font-size:14.5px;line-height:1.3;margin-top:10px}
.section-title{font-family:"Archivo",sans-serif;font-weight:400;font-size:24px;color:var(--maroon-deep);margin-top:10px}
.section-title b{font-weight:900}
.when-list{display:grid;grid-template-columns:1fr 1fr;row-gap:6px;column-gap:20px;margin-top:6px;list-style:none}
.when-list li{display:flex;align-items:center;gap:18px;font-size:11.5px;height:33px}
.when-icon{width:33px;height:33px;border-radius:50%;flex:none;border:2px solid var(--maroon);background:var(--maroon-deep)}
.when-icon--teal{border-color:var(--teal);background:var(--teal)}

.steps{margin-top:14px;background:var(--teal-deep);padding:36px 14px 12px;position:relative}
.steps__title{position:absolute;top:0;left:34px;right:34px;height:32px;background:var(--maroon);border-radius:0 0 14px 14px;color:#fff;text-align:center;font-family:"Archivo",sans-serif;font-weight:800;font-size:24px;line-height:32px}
.steps__grid{display:grid;grid-template-columns:repeat(3,1fr);grid-template-rows:84px 84px}
.step{display:flex;align-items:center;gap:6px;color:#fff;padding:0 6px;border-right:1px solid rgba(255,255,255,.3)}
.step:nth-child(3n){border-right:none}
.step:nth-child(-n+3){border-bottom:1px solid rgba(255,255,255,.3)}
.step__num{font-family:"Archivo",sans-serif;font-weight:900;font-size:36px;width:34px;flex:none}
.step__art{width:70px;height:70px;border-radius:50%;flex:none;background:radial-gradient(circle at 45% 40%,#f7c99a,#e9a06b 60%,#ffffff 61%)}
.step__text{font-size:11px;line-height:1.2}

.skin-title,.extra-title{font-family:"Archivo",sans-serif;font-weight:900;font-size:19px;color:var(--teal-deep);line-height:1.15;margin-top:10px}
.extra-title{margin-top:16px}
.ticks{list-style:none;font-size:11px;line-height:1.3}
.ticks li{display:flex;gap:8px;align-items:flex-start}
.ticks svg{flex:none;margin-top:2px}
.skin-list{display:grid;grid-template-columns:150px 180px 1fr;gap:10px;margin-top:8px}
.extra-list{display:grid;grid-template-columns:1fr 1fr;column-gap:40px;row-gap:6px;margin-top:8px}
.extra-list li{font-weight:600}
.extra-list .col{display:flex;flex-direction:column;gap:8px}

.footer{display:grid;grid-template-columns:330px 1fr;gap:16px;margin-top:22px}
.info-box{background:var(--maroon-deep);color:#fff;font-size:10.5px;text-align:center;padding:5px;line-height:1.35}
.funding{font-size:7.5px;line-height:1.3;margin-top:8px;color:var(--muted)}
.find-box{background:var(--teal);color:#fff;font-family:"Archivo",sans-serif;font-weight:800;font-size:16px;padding:6px 14px}
.find-lead{font-size:7.5px;font-weight:600;margin-top:6px}
.find-list{list-style:none;font-size:7.5px;line-height:1.45;color:var(--muted)}
.find-list li::before{content:"• ";color:var(--teal)}
</style>
</head>
<body>

<!-- Variant: COVID-19 -->
<article class="poster poster--covid">
  <header class="masthead">
    <div class="masthead__brand">
      <div class="campaign-frame"><div class="campaign-frame__name">LANTERN</div><div class="campaign-frame__sub">COVID-19 VACCINATION CAMPAIGN</div></div>
      <p class="masthead__tagline">PROTECT YOUR COMMUNITY. PROTECT YOUR ELDERS. STAY VACCINATED.</p>
    </div>
    <div class="masthead__partner"><div class="partner-mark"></div><div class="partner-name">NORTHERN CIRCLE<br>ELDERS ALLIANCE</div></div>
  </header>
  <div class="band"></div>
  <main class="content">
    <h1 class="headline"><span class="headline__top">CLEAN HANDS FOR A</span><span class="headline__bottom">HEALTHIER COMMUNITY</span></h1>
    <p class="intro">Viruses, like the flu and COIVD-19, can spread when hands touch people or surfaces. Regular handwashing with soap and water can help prevent you and others from getting sick.</p>
    <h2 class="section-title">WHEN TO <b>WASH YOUR HANDS:</b></h2>
    <ul class="when-list">
      <li><span class="when-icon" role="img" aria-label="Icon of a person coughing"></span>After coughing, sneezing, or blowing your nose</li>
      <li><span class="when-icon" role="img" aria-label="Icon of a toilet"></span>After toilet use, or changing diapers</li>
      <li><span class="when-icon when-icon--teal" role="img" aria-label="Icon of caring hands"></span>When caring for someone who is sick</li>
      <li><span class="when-icon when-icon--teal" role="img" aria-label="Icon of a dirty hand"></span>When hands are visibly dirty</li>
      <li><span class="when-icon" role="img" aria-label="Icon of a cooking pot"></span>Before, during and after you prepare food</li>
      <li><span class="when-icon" role="img" aria-label="Icon of a person with a pet"></span>After handling animals or animal waste</li>
      <li><span class="when-icon when-icon--teal" role="img" aria-label="Icon of a person eating"></span>Before eating</li>
      <li><span class="when-icon when-icon--teal" role="img" aria-label="Icon of a person walking"></span>Returning home after being in public</li>
    </ul>
    <section class="steps">
      <h2 class="steps__title">HOW TO WASH YOUR HANDS PROPERLY:</h2>
      <div class="steps__grid">
        <div class="step"><span class="step__num">1.</span><span class="step__art" role="img" aria-label="Illustration of hands under a tap"></span><span class="step__text">Wet your hands.</span></div>
        <div class="step"><span class="step__num">2.</span><span class="step__art" role="img" aria-label="Illustration of a hand pressing a soap pump"></span><span class="step__text">Apply soap.</span></div>
        <div class="step"><span class="step__num">3.</span><span class="step__art" role="img" aria-label="Illustration of hands rubbing together"></span><span class="step__text">Rub hands, wrists, and betweenfingers rapidly, and scrub under fingernails.</span></div>
        <div class="step"><span class="step__num">4.</span><span class="step__art" role="img" aria-label="Illustration of hands scrubbing with lather"></span><span class="step__text">Scrub for at least 20 seconds, or sing “Happy Birthday!” twice.</span></div>
        <div class="step"><span class="step__num">5.</span><span class="step__art" role="img" aria-label="Illustration of hands rinsing under a tap"></span><span class="step__text">Rinse your hands.</span></div>
        <div class="step"><span class="step__num">6.</span><span class="step__art" role="img" aria-label="Illustration of hands drying with a towel"></span><span class="step__text">Dry with air or a paper towel. Turn off the tap with a towel.</span></div>
      </div>
    </section>
    <h2 class="skin-title">SKIN PROTECTS THE BODY AGAIN VIRUSES. TAKE CARE OF THE SKIN ON YOUR HANDSTTTTT BY,</h2>
    <ul class="ticks skin-list">
      <li><svg width="10" height="10" viewBox="0 0 10 10"><circle cx="5" cy="5" r="5" fill="#8b2a2e"/><path d="M2.5 5l1.8 1.8L7.6 3.3" stroke="#fff" stroke-width="1.4" fill="none"/></svg>Applying water-based hand cream</li>
      <li><svg width="10" height="10" viewBox="0 0 10 10"><circle cx="5" cy="5" r="5" fill="#8b2a2e"/><path d="M2.5 5l1.8 1.8L7.6 3.3" stroke="#fff" stroke-width="1.4" fill="none"/></svg>Contact your doctor if your skin becomes irritated or infected</li>
      <li><svg width="10" height="10" viewBox="0 0 10 10"><circle cx="5" cy="5" r="5" fill="#8b2a2e"/><path d="M2.5 5l1.8 1.8L7.6 3.3" stroke="#fff" stroke-width="1.4" fill="none"/></svg>Use gloves during daily tasks, like when washing dishes, cooking, gardening, working on cars, or house repairs.</li>
    </ul>
    <h2 class="extra-title">ADDITIONAL WAYS TO PREVENT VIRUSES FROM SPREADING:</h2>
    <div class="extra-list">
      <ul class="ticks col">
        <li><svg width="10" height="10" viewBox="0 0 10 10"><circle cx="5" cy="5" r="5" fill="#8b2a2e"/><path d="M2.5 5l1.8 1.8L7.6 3.3" stroke="#fff" stroke-width="1.4" fill="none"/></svg>When you cough or sneeze, cover your mouth and nose with your elbow or a tissue.</li>
        <li><svg width="10" height="10" viewBox="0 0 10 10"><circle cx="5" cy="5" r="5" fill="#8b2a2e"/><path d="M2.5 5l1.8 1.8L7.6 3.3" stroke="#fff" stroke-width="1.4" fill="none"/></svg>Don’t touch your eyes, nose, or mouth.</li>
        <li><svg width="10" height="10" viewBox="0 0 10 10"><circle cx="5" cy="5" r="5" fill="#8b2a2e"/><path d="M2.5 5l1.8 1.8L7.6 3.3" stroke="#fff" stroke-width="1.4" fill="none"/></svg>Avoid close contact with those who are sick.</li>
      </ul>
      <ul class="ticks col">
        <li><svg width="10" height="10" viewBox="0 0 10 10"><circle cx="5" cy="5" r="5" fill="#8b2a2e"/><path d="M2.5 5l1.8 1.8L7.6 3.3" stroke="#fff" stroke-width="1.4" fill="none"/></svg>Wear a mask.</li>
        <li><svg width="10" height="10" viewBox="0 0 10 10"><circle cx="5" cy="5" r="5" fill="#8b2a2e"/><path d="M2.5 5l1.8 1.8L7.6 3.3" stroke="#fff" stroke-width="1.4" fill="none"/></svg>Use hand sanitizer if you are unable to wash your hands.</li>
        <li><svg width="10" height="10" viewBox="0 0 10 10"><circle cx="5" cy="5" r="5" fill="#8b2a2e"/><path d="M2.5 5l1.8 1.8L7.6 3.3" stroke="#fff" stroke-width="1.4" fill="none"/></svg>Get yearly vaccinations and stay up to date with vaccination boosters.</li>
      </ul>
    </div>
    <footer class="footer">
      <div>
        <p class="info-box">FOR MORE INFORMATION ON HANDWASHING,<br>visit: https://www.wellnessbureau.example/handwashing</p>
        <p class="funding">This project is supported by the Marlowe Bureau for Wellness Monitoring and Outreach of the Kestrel Office of Community Vitality and Care (KOV) as part of a financial assistance award totaling <b>$18,420,150 with 100 percent funded by MBW/KOV.</b> The contents are those of the author(s) and do not necessarily represent the official views of, nor an endorsement, by MBW/KOV, or the Kestrel Commonwealth Government.</p>
      </div>
      <div>
        <p class="find-box">FIND A VACCINATION SITE TODAY!</p>
        <p class="find-lead">To find out more about the available vaccines near you, contact your local:</p>
        <ul class="find-list">
          <li>Tribal Health Services, tribal, or urban health clinics, and doctor’s offices (even if you don’t have a regular doctor or nurse)</li>
          <li>Community Health Representative or Community Health Aide</li>
          <li>Visiting mobile and community-based immunization clinics, or</li>
          <li>Pharmacies, or grocery stores.</li>
        </ul>
      </div>
    </footer>
  </main>
  <div class="band band--foot"></div>
</article>

<!-- Variant: COVID-19 & Flu -->
<article class="poster poster--combo">
  <header class="masthead">
    <div class="masthead__brand">
      <div class="campaign-frame"><div class="campaign-frame__name">LANTERN</div><div class="campaign-frame__sub">COVID-19 &amp; FLU VACCINATION CAMPAIGN</div></div>
      <p class="masthead__tagline">PROTECT YOUR COMMUNITY. PROTECT YOUR ELDERS. STAY VACCINATED.</p>
    </div>
    <div class="masthead__partner"><div class="partner-mark"></div><div class="partner-name">NORTHERN CIRCLE<br>ELDERS ALLIANCE</div></div>
  </header>
  <div class="band"></div>
  <main class="content">
    <h1 class="headline"><span class="headline__top">CLEAN HANDS FOR A</span><span class="headline__bottom">HEALTHIER COMMUNITY</span></h1>
    <p class="intro">Viruses, like the flu and COIVD-19, can spread when hands touch people or surfaces. Regular handwashing with soap and water can help prevent you and others from getting sick.</p>
    <h2 class="section-title">WHEN TO <b>WASH YOUR HANDS:</b></h2>
    <ul class="when-list">
      <li><span class="when-icon" role="img" aria-label="Icon of a person coughing"></span>After coughing, sneezing, or blowing your nose</li>
      <li><span class="when-icon" role="img" aria-label="Icon of a toilet"></span>After toilet use, or changing diapers</li>
      <li><span class="when-icon when-icon--teal" role="img" aria-label="Icon of caring hands"></span>When caring for someone who is sick</li>
      <li><span class="when-icon when-icon--teal" role="img" aria-label="Icon of a dirty hand"></span>When hands are visibly dirty</li>
      <li><span class="when-icon" role="img" aria-label="Icon of a cooking pot"></span>Before, during and after you prepare food</li>
      <li><span class="when-icon" role="img" aria-label="Icon of a person with a pet"></span>After handling animals or animal waste</li>
      <li><span class="when-icon when-icon--teal" role="img" aria-label="Icon of a person eating"></span>Before eating</li>
      <li><span class="when-icon when-icon--teal" role="img" aria-label="Icon of a person walking"></span>Returning home after being in public</li>
    </ul>
    <section class="steps">
      <h2 class="steps__title">HOW TO WASH YOUR HANDS PROPERLY:</h2>
      <div class="steps__grid">
        <div class="step"><span class="step__num">1.</span><span class="step__art" role="img" aria-label="Illustration of hands under a tap"></span><span class="step__text">Wet your hands.</span></div>
        <div class="step"><span class="step__num">2.</span><span class="step__art" role="img" aria-label="Illustration of a hand pressing a soap pump"></span><span class="step__text">Apply soap.</span></div>
        <div class="step"><span class="step__num">3.</span><span class="step__art" role="img" aria-label="Illustration of hands rubbing together"></span><span class="step__text">Rub hands, wrists, and betweenfingers rapidly, and scrub under fingernails.</span></div>
        <div class="step"><span class="step__num">4.</span><span class="step__art" role="img" aria-label="Illustration of hands scrubbing with lather"></span><span class="step__text">Scrub for at least 20 seconds, or sing “Happy Birthday!” twice.</span></div>
        <div class="step"><span class="step__num">5.</span><span class="step__art" role="img" aria-label="Illustration of hands rinsing under a tap"></span><span class="step__text">Rinse your hands.</span></div>
        <div class="step"><span class="step__num">6.</span><span class="step__art" role="img" aria-label="Illustration of hands drying with a towel"></span><span class="step__text">Dry with air or a paper towel. Turn off the tap with a towel.</span></div>
      </div>
    </section>
    <h2 class="skin-title">SKIN PROTECTS THE BODY AGAIN VIRUSES. TAKE CARE OF THE SKIN ON YOUR HANDSTTTTT BY,</h2>
    <ul class="ticks skin-list">
      <li><svg width="10" height="10" viewBox="0 0 10 10"><circle cx="5" cy="5" r="5" fill="#8b2a2e"/><path d="M2.5 5l1.8 1.8L7.6 3.3" stroke="#fff" stroke-width="1.4" fill="none"/></svg>Applying water-based hand cream</li>
      <li><svg width="10" height="10" viewBox="0 0 10 10"><circle cx="5" cy="5" r="5" fill="#8b2a2e"/><path d="M2.5 5l1.8 1.8L7.6 3.3" stroke="#fff" stroke-width="1.4" fill="none"/></svg>Contact your doctor if your skin becomes irritated or infected</li>
      <li><svg width="10" height="10" viewBox="0 0 10 10"><circle cx="5" cy="5" r="5" fill="#8b2a2e"/><path d="M2.5 5l1.8 1.8L7.6 3.3" stroke="#fff" stroke-width="1.4" fill="none"/></svg>Use gloves during daily tasks, like when washing dishes, cooking, gardening, working on cars, or house repairs.</li>
    </ul>
    <h2 class="extra-title">ADDITIONAL WAYS TO PREVENT VIRUSES FROM SPREADING:</h2>
    <div class="extra-list">
      <ul class="ticks col">
        <li><svg width="10" height="10" viewBox="0 0 10 10"><circle cx="5" cy="5" r="5" fill="#8b2a2e"/><path d="M2.5 5l1.8 1.8L7.6 3.3" stroke="#fff" stroke-width="1.4" fill="none"/></svg>When you cough or sneeze, cover your mouth and nose with your elbow or a tissue.</li>
        <li><svg width="10" height="10" viewBox="0 0 10 10"><circle cx="5" cy="5" r="5" fill="#8b2a2e"/><path d="M2.5 5l1.8 1.8L7.6 3.3" stroke="#fff" stroke-width="1.4" fill="none"/></svg>Don’t touch your eyes, nose, or mouth.</li>
        <li><svg width="10" height="10" viewBox="0 0 10 10"><circle cx="5" cy="5" r="5" fill="#8b2a2e"/><path d="M2.5 5l1.8 1.8L7.6 3.3" stroke="#fff" stroke-width="1.4" fill="none"/></svg>Avoid close contact with those who are sick.</li>
      </ul>
      <ul class="ticks col">
        <li><svg width="10" height="10" viewBox="0 0 10 10"><circle cx="5" cy="5" r="5" fill="#8b2a2e"/><path d="M2.5 5l1.8 1.8L7.6 3.3" stroke="#fff" stroke-width="1.4" fill="none"/></svg>Wear a mask.</li>
        <li><svg width="10" height="10" viewBox="0 0 10 10"><circle cx="5" cy="5" r="5" fill="#8b2a2e"/><path d="M2.5 5l1.8 1.8L7.6 3.3" stroke="#fff" stroke-width="1.4" fill="none"/></svg>Use hand sanitizer if you are unable to wash your hands.</li>
        <li><svg width="10" height="10" viewBox="0 0 10 10"><circle cx="5" cy="5" r="5" fill="#8b2a2e"/><path d="M2.5 5l1.8 1.8L7.6 3.3" stroke="#fff" stroke-width="1.4" fill="none"/></svg>Get yearly vaccinations and stay up to date with vaccination boosters.</li>
      </ul>
    </div>
    <footer class="footer">
      <div>
        <p class="info-box">FOR MORE INFORMATION ON HANDWASHING,<br>visit: https://www.wellnessbureau.example/handwashing</p>
        <p class="funding">This project is supported by the Marlowe Bureau for Wellness Monitoring and Outreach of the Kestrel Office of Community Vitality and Care (KOV) as part of a financial assistance award totaling <b>$18,420,150 with 100 percent funded by MBW/KOV.</b> The contents are those of the author(s) and do not necessarily represent the official views of, nor an endorsement, by MBW/KOV, or the Kestrel Commonwealth Government.</p>
      </div>
      <div>
        <p class="find-box">FIND A VACCINATION SITE TODAY!</p>
        <p class="find-lead">To find out more about the available vaccines near you, contact your local:</p>
        <ul class="find-list">
          <li>Tribal Health Services, tribal, or urban health clinics, and doctor’s offices (even if you don’t have a regular doctor or nurse)</li>
          <li>Community Health Representative or Community Health Aide</li>
          <li>Visiting mobile and community-based immunization clinics, or</li>
          <li>Pharmacies, or grocery stores.</li>
        </ul>
      </div>
    </footer>
  </main>
  <div class="band band--foot"></div>
</article>

<!-- Variant: COVID-19 (alternate) -->
<article class="poster poster--covid-b">
  <header class="masthead">
    <div class="masthead__brand">
      <div class="campaign-frame"><div class="campaign-frame__name">LANTERN</div><div class="campaign-frame__sub">COVID-19 VACCINATION CAMPAIGN</div></div>
      <p class="masthead__tagline">PROTECT YOUR COMMUNITY. PROTECT YOUR ELDERS. STAY VACCINATED.</p>
    </div>
    <div class="masthead__partner"><div class="partner-mark"></div><div class="partner-name">NORTHERN CIRCLE<br>ELDERS ALLIANCE</div></div>
  </header>
  <div class="band"></div>
  <main class="content">
    <h1 class="headline"><span class="headline__top">CLEAN HANDS FOR A</span><span class="headline__bottom">HEALTHIER COMMUNITY</span></h1>
    <p class="intro">Viruses, like the flu and COIVD-19, can spread when hands touch people or surfaces. Regular handwashing with soap and water can help prevent you and others from getting sick.</p>
    <h2 class="section-title">WHEN TO <b>WASH YOUR HANDS:</b></h2>
    <ul class="when-list">
      <li><span class="when-icon" role="img" aria-label="Icon of a person coughing"></span>After coughing, sneezing, or blowing your nose</li>
      <li><span class="when-icon" role="img" aria-label="Icon of a toilet"></span>After toilet use, or changing diapers</li>
      <li><span class="when-icon when-icon--teal" role="img" aria-label="Icon of caring hands"></span>When caring for someone who is sick</li>
      <li><span class="when-icon when-icon--teal" role="img" aria-label="Icon of a dirty hand"></span>When hands are visibly dirty</li>
      <li><span class="when-icon" role="img" aria-label="Icon of a cooking pot"></span>Before, during and after you prepare food</li>
      <li><span class="when-icon" role="img" aria-label="Icon of a person with a pet"></span>After handling animals or animal waste</li>
      <li><span class="when-icon when-icon--teal" role="img" aria-label="Icon of a person eating"></span>Before eating</li>
      <li><span class="when-icon when-icon--teal" role="img" aria-label="Icon of a person walking"></span>Returning home after being in public</li>
    </ul>
    <section class="steps">
      <h2 class="steps__title">HOW TO WASH YOUR HANDS PROPERLY:</h2>
      <div class="steps__grid">
        <div class="step"><span class="step__num">1.</span><span class="step__art" role="img" aria-label="Illustration of hands under a tap"></span><span class="step__text">Wet your hands.</span></div>
        <div class="step"><span class="step__num">2.</span><span class="step__art" role="img" aria-label="Illustration of a hand pressing a soap pump"></span><span class="step__text">Apply soap.</span></div>
        <div class="step"><span class="step__num">3.</span><span class="step__art" role="img" aria-label="Illustration of hands rubbing together"></span><span class="step__text">Rub hands, wrists, and betweenfingers rapidly, and scrub under fingernails.</span></div>
        <div class="step"><span class="step__num">4.</span><span class="step__art" role="img" aria-label="Illustration of hands scrubbing with lather"></span><span class="step__text">Scrub for at least 20 seconds, or sing “Happy Birthday!” twice.</span></div>
        <div class="step"><span class="step__num">5.</span><span class="step__art" role="img" aria-label="Illustration of hands rinsing under a tap"></span><span class="step__text">Rinse your hands.</span></div>
        <div class="step"><span class="step__num">6.</span><span class="step__art" role="img" aria-label="Illustration of hands drying with a towel"></span><span class="step__text">Dry with air or a paper towel. Turn off the tap with a towel.</span></div>
      </div>
    </section>
    <h2 class="skin-title">SKIN PROTECTS THE BODY AGAIN VIRUSES. TAKE CARE OF THE SKIN ON YOUR HANDSTTTTT BY,</h2>
    <ul class="ticks skin-list">
      <li><svg width="10" height="10" viewBox="0 0 10 10"><circle cx="5" cy="5" r="5" fill="#8b2a2e"/><path d="M2.5 5l1.8 1.8L7.6 3.3" stroke="#fff" stroke-width="1.4" fill="none"/></svg>Applying water-based hand cream</li>
      <li><svg width="10" height="10" viewBox="0 0 10 10"><circle cx="5" cy="5" r="5" fill="#8b2a2e"/><path d="M2.5 5l1.8 1.8L7.6 3.3" stroke="#fff" stroke-width="1.4" fill="none"/></svg>Contact your doctor if your skin becomes irritated or infected</li>
      <li><svg width="10" height="10" viewBox="0 0 10 10"><circle cx="5" cy="5" r="5" fill="#8b2a2e"/><path d="M2.5 5l1.8 1.8L7.6 3.3" stroke="#fff" stroke-width="1.4" fill="none"/></svg>Use gloves during daily tasks, like when washing dishes, cooking, gardening, working on cars, or house repairs.</li>
    </ul>
    <h2 class="extra-title">ADDITIONAL WAYS TO PREVENT VIRUSES FROM SPREADING:</h2>
    <div class="extra-list">
      <ul class="ticks col">
        <li><svg width="10" height="10" viewBox="0 0 10 10"><circle cx="5" cy="5" r="5" fill="#8b2a2e"/><path d="M2.5 5l1.8 1.8L7.6 3.3" stroke="#fff" stroke-width="1.4" fill="none"/></svg>When you cough or sneeze, cover your mouth and nose with your elbow or a tissue.</li>
        <li><svg width="10" height="10" viewBox="0 0 10 10"><circle cx="5" cy="5" r="5" fill="#8b2a2e"/><path d="M2.5 5l1.8 1.8L7.6 3.3" stroke="#fff" stroke-width="1.4" fill="none"/></svg>Don’t touch your eyes, nose, or mouth.</li>
        <li><svg width="10" height="10" viewBox="0 0 10 10"><circle cx="5" cy="5" r="5" fill="#8b2a2e"/><path d="M2.5 5l1.8 1.8L7.6 3.3" stroke="#fff" stroke-width="1.4" fill="none"/></svg>Avoid close contact with those who are sick.</li>
      </ul>
      <ul class="ticks col">
        <li><svg width="10" height="10" viewBox="0 0 10 10"><circle cx="5" cy="5" r="5" fill="#8b2a2e"/><path d="M2.5 5l1.8 1.8L7.6 3.3" stroke="#fff" stroke-width="1.4" fill="none"/></svg>Wear a mask.</li>
        <li><svg width="10" height="10" viewBox="0 0 10 10"><circle cx="5" cy="5" r="5" fill="#8b2a2e"/><path d="M2.5 5l1.8 1.8L7.6 3.3" stroke="#fff" stroke-width="1.4" fill="none"/></svg>Use hand sanitizer if you are unable to wash your hands.</li>
        <li><svg width="10" height="10" viewBox="0 0 10 10"><circle cx="5" cy="5" r="5" fill="#8b2a2e"/><path d="M2.5 5l1.8 1.8L7.6 3.3" stroke="#fff" stroke-width="1.4" fill="none"/></svg>Get yearly vaccinations and stay up to date with vaccination boosters.</li>
      </ul>
    </div>
    <footer class="footer">
      <div>
        <p class="info-box">FOR MORE INFORMATION ON HANDWASHING,<br>visit: https://www.wellnessbureau.example/handwashing</p>
        <p class="funding">This project is supported by the Marlowe Bureau for Wellness Monitoring and Outreach of the Kestrel Office of Community Vitality and Care (KOV) as part of a financial assistance award totaling <b>$18,420,150 with 100 percent funded by MBW/KOV.</b> The contents are those of the author(s) and do not necessarily represent the official views of, nor an endorsement, by MBW/KOV, or the Kestrel Commonwealth Government.</p>
      </div>
      <div>
        <p class="find-box">FIND A VACCINATION SITE TODAY!</p>
        <p class="find-lead">To find out more about the available vaccines near you, contact your local:</p>
        <ul class="find-list">
          <li>Tribal Health Services, tribal, or urban health clinics, and doctor’s offices (even if you don’t have a regular doctor or nurse)</li>
          <li>Community Health Representative or Community Health Aide</li>
          <li>Visiting mobile and community-based immunization clinics, or</li>
          <li>Pharmacies, or grocery stores.</li>
        </ul>
      </div>
    </footer>
  </main>
  <div class="band band--foot"></div>
</article>

</body>
</html>
```